Book for a presidential campaign

We need a book front cover design for a presidential campaign. The title of the book is "Raise Every Harbor Higher!" Subtitle is "Notes From a Quiet Orchard" The candidate's name should be on the cover as well, so let's call him "Dorian Falke" so you have a name to use in your design. The candidate is nonpartisan, appealing to both liberals and conservatives. The solutions are out of the box and powerful, leading to the benefit of all.

```html
<!DOCTYPE html>
<html lang="en">
<head>
<meta charset="utf-8">
<title>Raise Every Harbor Higher! — Dorian Falke</title>
<link rel="stylesheet" href="https://fonts.googleapis.com/css2?family=Cinzel:wght@700;900&family=Arimo:wght@400&display=swap">
<style>
  :root {
    --gold-deep: #d6a525;
    --gold-mid: #e8c45a;
    --gold-pale: #f8eda6;
    --ink: #1c1a18;
    --cover-black: #221f1f;
    --cream: #f6e7a0;
    --rule-gold: #c9a53a;
    --coin-hi: #f4d25c;
    --coin-lo: #b8860b;
  }
  * { margin: 0; padding: 0; box-sizing: border-box; }
  html, body { width: 848px; height: 1200px; overflow: hidden; background: #ffffff; }
  .cover {
    position: relative;
    width: 848px;
    height: 1200px;
    background: var(--cover-black);
    overflow: hidden;
  }
  .title-band {
    position: absolute;
    left: 0; top: 0;
    width: 100%; height: 480px;
    background: linear-gradient(to bottom, var(--gold-deep) 0%, var(--gold-mid) 45%, var(--gold-pale) 100%);
    display: flex;
    flex-direction: column;
    align-items: center;
    justify-content: center;
    padding-top: 30px;
  }
  .title {
    font-family: "Cinzel", serif;
    font-weight: 900;
    color: var(--ink);
    text-align: center;
    line-height: 1;
  }
  .title-line { display: block; font-size: 84px; letter-spacing: 1px; }
  .title-small { display: block; font-size: 40px; margin: 14px 0 10px; }
  .subtitle {
    position: absolute;
    top: 515px; left: 0; width: 100%;
    font-family: "Arimo", sans-serif;
    font-size: 30px;
    letter-spacing: 1px;
    color: var(--cream);
    text-align: center;
    text-transform: uppercase;
  }
  .coins-art {
    position: absolute;
    left: 214px; top: 610px;
    width: 420px; height: 340px;
    border-radius: 10px;
    background: radial-gradient(ellipse at 45% 40%, var(--coin-hi) 0%, #d9a830 45%, var(--coin-lo) 80%, rgba(184,134,11,0) 100%);
  }
  .byline {
    position: absolute;
    top: 1010px; left: 0; width: 100%;
    display: flex; align-items: center; justify-content: center;
    gap: 22px;
  }
  .byline-rule { width: 220px; height: 2px; background: var(--rule-gold); }
  .author {
    font-family: "Arimo", sans-serif;
    font-size: 32px;
    letter-spacing: 1px;
    color: var(--cream);
    text-transform: uppercase;
  }
  .base-rule {
    position: absolute;
    left: 0; top: 1110px;
    width: 100%; height: 2px;
    background: var(--rule-gold);
  }
</style>
</head>
<body>
  <main class="cover">
    <header class="title-band">
      <h1 class="title">
        <span class="title-line">RAISE EVERY</span>
        <span class="title-small">HARBOR</span>
        <span class="title-line">HIGHER!</span>
      </h1>
    </header>
    <p class="subtitle">Notes From a Quiet Orchard</p>
    <div class="coins-art" role="img" aria-label="Illustration of stacked shining gold coins"></div>
    <div class="byline">
      <span class="byline-rule"></span>
      <span class="author">Dorian Falke</span>
      <span class="byline-rule"></span>
    </div>
    <div class="base-rule"></div>
  </main>
</body>
</html>
```